Brandvik Marksfield Indoor shooting range

Brandvik Marksfield LTD is looking for web page, wich itroduces company, and mainly indoor shooting range. Weapon rentals, ammunition, corporate clients welcome, OKRV (orvelian kestrel range ventureship) orienteted shooters welcome. Colors of webpage black and white/ camo green accents. needs to be in 3 languages, russian, english and estonian.

Target Market(s)

incoming tourist, newcomers and sophisticated shooters

Requirements
Must have
• booking calender by hourly, direction page. Okrv logos

```html
<!DOCTYPE html>
<html lang="en">
<head>
<meta charset="utf-8">
<title>Brandvik Marksfield – Indoor Shooting Range</title>
<link rel="stylesheet" href="https://fonts.googleapis.com/css2?family=Open+Sans:ital,wght@0,400;0,600;0,700;1,600&display=swap">
<style>
:root{
  --page:#f1f1ef;
  --ink:#1a1a1a;
  --camo:#6a7a45;
  --camo-dark:#2f4a25;
  --nav:#141414;
  --text:#555;
  --white:#fff;
  --footer:#d8d8d8;
  --teal:#7fb5b5;
}
*{box-sizing:border-box;margin:0;padding:0}
html,body{width:800px;height:1200px;overflow:hidden}
body{position:relative;background:var(--page);font-family:"Open Sans",Arial,sans-serif;color:var(--ink)}
.abs{position:absolute}

.brand{left:58px;top:25px;width:175px;text-align:center;color:var(--camo);font-weight:600;font-size:25px;line-height:21px}
.hq{left:635px;top:20px;font-size:11.5px;line-height:12.5px;color:#b7b7b7}
.hq strong{color:#666;font-weight:600;font-size:12px}

.nav{left:58px;top:91px;width:682px;height:36px;background:linear-gradient(#222,var(--nav));display:flex;align-items:center;padding-left:26px;gap:30px}
.nav a{color:var(--white);text-decoration:none;font-size:11.5px;font-weight:600;letter-spacing:.2px}
.nav a.active{color:#999;font-weight:400}

.hero{left:58px;top:127px;width:682px;height:400px;background:
  radial-gradient(ellipse 30% 40% at 82% 62%,#cfcfca 0%,#8e8e8a 40%,transparent 100%),
  radial-gradient(ellipse 28% 30% at 62% 22%,#4a4d55 0%,transparent 100%),
  radial-gradient(ellipse 40% 25% at 40% 62%,#3c4046 0%,transparent 100%),
  linear-gradient(90deg,#0c0c0e,#151517 50%,#1d1d1f);
  -webkit-mask:linear-gradient(#000 85%,transparent);mask:linear-gradient(#000 85%,transparent)}

.card{top:377px;width:207px;height:248px;background:linear-gradient(#191919,#050505);border-top:3px solid var(--camo-dark)}
.card .photo{height:116px}
.photo.rentals{background:radial-gradient(ellipse 70% 45% at 55% 50%,#6a6d70,#2a2b2d 60%,#0e0e0f)}
.photo.range{background:linear-gradient(90deg,#58606a 0%,#c9cdd2 12%,#8a8f96 28%,#a9b0ba 45%,#6f7780 62%,#b9bfc7 80%,#7b828b 100%)}
.photo.corporate{background:linear-gradient(90deg,#2a2624 0%,#3a3430 35%,#bfbfbf 55%,#eeeeee 75%,#d8d6d4 100%)}
.card .title{position:absolute;left:10px;top:122px;color:var(--camo);font-weight:700;font-size:27px;line-height:30px}
.card .sub{position:absolute;right:12px;top:146px;color:var(--white);font-size:16.5px;letter-spacing:.5px}
.card p{position:absolute;left:14px;top:170px;width:180px;color:#cfcfcf;font-size:8.6px;line-height:11.6px}
.card .more{position:absolute;left:13px;top:216px;width:63px;height:20px;background:linear-gradient(#fafafa,#cfcfcf);clip-path:polygon(0 0,88% 0,100% 50%,88% 100%,0 100%);font-size:8.6px;font-weight:600;color:#333;line-height:20px;padding-left:5px}

.content{left:0;top:678px;width:800px;height:350px;background:var(--white)}
.welcome{left:86px;top:702px;width:330px}
.welcome h1{font-style:italic;font-weight:600;font-size:23px;letter-spacing:1.6px}
.welcome p{margin-top:9px;font-size:9.5px;line-height:12px;letter-spacing:.5px;color:var(--text)}
.book{left:562px;top:706px;font-size:20px;letter-spacing:1.2px;font-weight:400}

.cal{left:557px;top:743px;width:121px;background:#e4e4e4;box-shadow:0 1px 2px rgba(0,0,0,.3);font-size:8px}
.cal .head{background:linear-gradient(#555,#333);color:#fff;text-align:center;height:14px;line-height:14px;font-size:7.5px;display:flex;justify-content:space-between;padding:0 4px}
.cal .dow{display:grid;grid-template-columns:repeat(7,1fr);background:#444;color:#ddd;font-size:4.5px;text-align:center;height:7px;line-height:7px}
.cal .wk{display:grid;grid-template-columns:repeat(7,1fr);gap:1px;padding:1px}
.cal .wk span{background:linear-gradient(#fff,#e2e2e2);text-align:center;font-weight:700;height:15px;line-height:15px;color:#222}
.cal .wk span.off{color:#bbb}
.cal .wk span.today{background:#666;color:#fff}
.cal .wk span.sel{background:var(--teal);color:#245}
.cal .events{background:var(--camo-dark);color:#e8efe0;font-size:4.6px;padding:2px 4px;line-height:6.3px}
.cal .events .row{display:flex;justify-content:space-between;padding-left:3px}

.footer{left:0;top:1027px;width:800px;height:173px;background:var(--footer)}
.partners{left:58px;top:928px;width:684px;height:118px;background:var(--white);border:1px solid #d3d3d3}
.partners h2{position:absolute;left:58px;top:15px;font-weight:400;font-size:20px;letter-spacing:2px}
.logos{position:absolute;left:60px;top:52px;width:590px;display:flex;justify-content:space-between;align-items:center;height:44px}
.logo{font-size:10.5px;font-weight:700;color:#333;display:flex;align-items:center;gap:4px;white-space:nowrap}
.logo i{display:block;width:26px;height:26px;background:#222;border-radius:50%}
.logo b{display:block;width:12px;height:12px;background:#444}

.col{top:1066px;font-size:8px;line-height:9.5px;color:#888;text-transform:uppercase}
.col h3{font-size:9.5px;font-weight:400;color:#444;text-transform:none;margin-bottom:8px}
.vline{left:487px;top:1062px;width:1px;height:82px;background:#aaa}
.signup{left:530px;top:1066px;font-size:9.5px;color:#444}
.signup .form{display:flex;gap:5px;margin-top:7px}
.signup .field{width:161px;height:16px;background:#fff;border:1px solid #bbb;font-size:6.5px;color:#aaa;line-height:14px;padding-left:6px}
.signup .btn{width:46px;height:16px;background:#bdbdbd;color:#444;font-size:8.5px;font-weight:600;text-align:center;line-height:16px}
.signup .follow{margin-top:7px}
.social{display:flex;gap:8px;margin-top:6px;font-size:7.5px;color:#555;align-items:center}
.social span{display:flex;align-items:center;gap:3px}
.social b{display:block;width:18px;height:18px;background:#555;border-radius:2px}
.rule{left:58px;top:1163px;width:684px;height:1px;background:#b9b9b9}
.copy{left:0;top:1175px;width:800px;text-align:center;font-size:9.5px;color:#999}
.copy strong{color:#333;font-weight:400}
</style>
</head>
<body>

<div class="abs brand">Brandvik<br>Marksfield</div>
<div class="abs hq">LTD Headquaters<br>Kaskadi 14, 10115<br>Tallinn, Estonia<br><strong>Tel : 37-200-5550147</strong></div>

<nav class="abs nav">
  <a class="active">HOME</a><a>SHOOTING RANGE</a><a>TRAINING</a><a>GALLERY</a><a>DIRECTIONS</a><a>ABOUT US</a><a>CONTACT US</a>
</nav>

<div class="abs hero" role="img" aria-label="Masked shooter in ear protection aiming a scoped rifle in a dark indoor range"></div>

<div class="abs card" style="left:75px">
  <div class="photo rentals" role="img" aria-label="Assault rifles laid out for rental"></div>
  <div class="title">Weapon</div><div class="sub">Rentals</div>
  <p>Lorem ipsum dolor sit amet, consectetur adipiscing elit. Donec mattis consequat massa, a rhoncus nunc facilisis vel.</p>
  <div class="more">Learn More</div>
</div>
<div class="abs card" style="left:296px">
  <div class="photo range" role="img" aria-label="Shooters standing at range lanes"></div>
  <div class="title">Shooting</div><div class="sub">Range</div>
  <p>Lorem ipsum dolor sit amet, consectetur adipiscing elit. Donec mattis consequat massa, a rhoncus nunc facilisis vel.</p>
  <div class="more">Learn More</div>
</div>
<div class="abs card" style="left:516px">
  <div class="photo corporate" role="img" aria-label="Shooter with ear defenders firing at a target lane"></div>
  <div class="title">Corporate</div><div class="sub">Clients</div>
  <p>Lorem ipsum dolor sit amet, consectetur adipiscing elit. Donec mattis consequat massa, a rhoncus nunc facilisis vel.</p>
  <div class="more">Learn More</div>
</div>

<div class="abs content"></div>
<section class="abs welcome">
  <h1>Welcome to LTD</h1>
  <p>Lorem ipsum dolor sit amet, consectetur adipiscing elit. Donec mattis consequat massa, a rhoncus nunc facilisis vel. Maecenas tristique orci dui. Cum sociis natoque penatibus et magnis dis parturient montes, nascetur ridiculus mus. Integer gravida egestas ante commodo mattis. Praesent ligula nisl, scelerisque et leo a, luctus vestibulum risus. Sed eu sapien vel dolor euismod porttitor lacinia sit amet arcu. Curabitur justo tellus, commodo vel nisl non, consectetur porta massa. Duis id tortor nunc. Vivamus tincidunt semper molestie. Nunc dictum bibendum augue at luctus. Donec dui sapien, pulvinar eget auctor vel, laoreet sagittis diam. Mauris porta diam augue, non ultrices arcu varius nec. Phasellus at leo egestas, pellentesque erat nec, sodales dui. Donec posuere enim at bibendum porttitor.</p>
</section>

<div class="abs book">Book Now</div>
<div class="abs cal">
  <div class="head"><span>◂</span><span>October 2012</span><span>▸</span></div>
  <div class="dow"><span>Mon</span><span>Tue</span><span>Wed</span><span>Thu</span><span>Fri</span><span>Sat</span><span>Sun</span></div>
  <div class="wk"><span class="off">29</span><span class="off">30</span><span class="off">31</span><span>1</span><span>2</span><span>3</span><span>4</span></div>
  <div class="wk"><span>5</span><span>6</span><span>7</span><span class="today">8</span><span>9</span><span>10</span><span>11</span></div>
  <div class="wk"><span>12</span><span>13</span><span>14</span><span>15</span><span>16</span><span>17</span><span>18</span></div>
  <div class="wk"><span>19</span><span>20</span><span>21</span><span>22</span><span>23</span><span class="sel">24</span><span>25</span></div>
  <div class="events">
    Range briefing
    <div class="row"><span>6:30 to 9:30 am</span><span>Lane Four Café</span></div>
    Walk the dog
    <div class="row"><span>6:30 to 9:30 pm</span><span>Park around the Corner</span></div>
  </div>
  <div class="wk"><span>26</span><span>27</span><span>28</span><span>29</span><span class="off">1</span><span class="off">2</span><span class="off">3</span></div>
</div>

<div class="abs footer"></div>
<section class="abs partners">
  <h2>Partners :</h2>
  <div class="logos">
    <div class="logo"><i aria-hidden="true"></i>OKRV</div>
    <div class="logo">Halvor Mart</div>
    <div class="logo">Stripe Lager</div>
    <div class="logo"><b></b>Norvale</div>
    <div class="logo">Keldor Auto</div>
    <div class="logo">Vellacom</div>
    <div class="logo">Astrid Motors</div>
  </div>
</section>

<div class="abs col" style="left:99px"><h3>Links</h3>Home<br>Shooting Range<br>Training<br>Gallery<br>Directions<br>About us<br>Contact us</div>
<div class="abs col" style="left:238px"><h3>My Account</h3>Access my account<br><span style="text-transform:none">Register</span></div>
<div class="abs col" style="left:351px"><h3>About LTD</h3>Our company<br>Careers<br>Business &amp; trade sales<br>Affiliate program<br>Shop our catalog</div>
<div class="abs vline"></div>
<div class="abs signup">
  Signup for Shooting Range Newsletters :
  <div class="form"><div class="field">Enter email address</div><div class="btn">Submit</div></div>
  <div class="follow">Follow us :</div>
  <div class="social"><span><b></b>Tattle</span><span><b></b>Chirpa</span><span><b></b>Plusly</span></div>
</div>
<div class="abs rule"></div>
<div class="abs copy"><strong>Brandvik Marksfield</strong> - Copyright 2013 | All rights reserved.</div>

</body>
</html>
```